Home Page for Prospix

We need to design a new home page for Prospix.com, a provider of B2B data for sales and marketing professionals.

The home page should follow the lead of our newly re-designed header and logo (still being tweaked) and use our new color scheme. Please refer to attached file. Please use this file as as the basis of the design for the rest or the home page. No part of the header or logo needs to be altered in this project.

All submissions should be clear, fresh, clean and simple in style. We like the look and feel of tallyvine.com, costharbor.com and pollquarry.com. Please use them as references.

The main functions of the home page will be to tell the user about 1) the benefits and uses of Prospix and 2) to get them to sign up.

Based upon the successful redesign of our homepage, we will also be redesigning our subscription page and our about us page in the coming weeks.

Target Market(s)

Sales and marketing professionals. Mostly 25 - 45 year old males.

Industry/Entity Type

Marketing

Requirements
Must have
• Items needed:

1A) There should be three main points highlighted 1) Fresh Data 2) Sales Intelligence 3) Increased Bottomline. There will be further text under these headers tbd. For style/feel reference the same device used by pollquarry uses on its homepage.

1B) When you rollover these three items they should highlight and be clickable. The click will lead you to a header and paragraph about each that is further down the homepage (text tbd).

2) We also need a free trial and a sign up button. This button should move with you as you scroll up and down the homepage. Reference www.tallyvine.com.

3) We need a “Featured In” section. Also reference tallyvine.com. You can pull the content from prospix.com’s current home page.

4) We also need a social media buttons section (chatterlane, quipstream, orbitly+ and workNest)

```html
<!DOCTYPE html>
<html lang="en">
<head>
<meta charset="utf-8">
<title>Prospix – B2B Sales Data</title>
<link rel="stylesheet" href="https://fonts.googleapis.com/css2?family=Arimo:ital,wght@0,400;0,700;1,400&display=swap">
<style>
:root{
  --page:#f6f6f6;
  --header-top:#6a6a6a;
  --header-bottom:#3d3d3d;
  --nav-blue:#0b95f2;
  --brand-blue:#1ea6e6;
  --orange:#ff8400;
  --orange-dark:#e5600c;
  --ink:#14202b;
  --muted:#8a8a8a;
  --line:#dcdcdc;
  --white:#ffffff;
  --panel-head-top:#2bb5ec;
  --panel-head-bottom:#1192d4;
  --footer-dark:#3c3c3c;
  --social-blue:#2e7cc4;
  --social-red:#d4473a;
}
*{box-sizing:border-box;margin:0;padding:0}
html,body{width:1200px;height:963px;overflow:hidden}
body{background:var(--page);font-family:"Arimo",Arial,sans-serif;position:relative;color:var(--ink)}
.abs{position:absolute}

.site-header{left:0;top:0;width:1200px;height:84px;background:linear-gradient(var(--header-top),var(--header-bottom))}
.brand{left:254px;top:16px;display:flex;align-items:center;gap:9px}
.brand-dot{width:28px;height:28px;border-radius:50%;background:var(--white)}
.brand-name{font-size:42px;font-weight:700;color:var(--brand-blue);letter-spacing:-1px;line-height:48px}

.main-nav{left:0;top:84px;width:1200px;height:29px;background:var(--nav-blue)}
.nav-item{position:absolute;top:0;height:29px;line-height:31px;text-align:center;color:var(--white);font-weight:700;font-size:15px;border-right:1px solid rgba(255,255,255,.75)}
.nav-item.active{background:var(--page);color:#333}
.search{left:716px;top:88px;width:254px;height:22px;border-radius:11px;background:var(--white);font-size:11px;color:#444;padding:5px 11px}

.login-box{left:771px;top:0;width:195px;height:131px;background:var(--orange);border-radius:0 0 5px 5px;box-shadow:0 2px 4px rgba(0,0,0,.25)}
.login-tabs{position:absolute;top:0;left:0;width:100%;height:23px;display:flex;font-size:11.5px;font-weight:700;color:var(--white);white-space:nowrap}
.login-tabs span{display:block;line-height:23px}
.login-tabs .tab-login{padding:0 8px 0 16px}
.login-tabs .tab-signup{border-left:1px solid rgba(255,255,255,.85);padding-left:8px}
.login-field{position:absolute;left:14px;width:165px;height:24px;background:var(--white);font-size:11px;font-style:italic;color:#444;padding:6px 11px}

.hero{left:130px;top:145px;width:940px;height:324px;border-radius:4px 4px 0 0;overflow:hidden;background:radial-gradient(circle at 70% 35%,#6d88aa 0,#3a5275 25%,#15243b 55%,#0b1526 100%)}
.hero-title{left:50px;top:87px;background:rgba(0,0,0,.75);color:var(--white);font-size:40px;font-weight:700;padding:0 9px;line-height:48px}
.hero-sub{left:50px;top:139px;background:rgba(0,0,0,.6);color:var(--white);font-size:30px;padding:0 8px;line-height:46px}
.cta{left:51px;top:221px;width:154px;height:46px;border-radius:4px;background:linear-gradient(#ff7a1c,var(--orange-dark));color:var(--white);font-size:19px;font-weight:700;text-align:center;line-height:46px;box-shadow:0 2px 3px rgba(0,0,0,.4)}
.slide-arrow{top:125px;width:76px;height:76px;border-radius:50%;background:var(--white);box-shadow:0 0 6px rgba(0,0,0,.35);color:var(--orange);font-size:24px;font-weight:700;line-height:76px}
.slide-arrow.prev{left:-38px;text-align:right;padding-right:19px}
.slide-arrow.next{left:902px;padding-left:17px}

.features{left:130px;top:469px;width:940px;height:140px;background:linear-gradient(var(--white),#f8f8f8);border:1px solid #e2e2e2;border-top:0;border-radius:0 0 4px 4px;box-shadow:0 1px 2px rgba(0,0,0,.1);display:flex}
.feature{position:relative;border-right:1px solid var(--line);padding:14px 30px 0 19px}
.feature:last-child{border-right:0;padding-left:14px}
.feature h2{font-size:18px;font-weight:700;margin-bottom:11px}
.feature p{font-size:14px;line-height:18px;color:var(--muted)}
.feature p b{color:#555}
.read-more{position:absolute;left:21px;top:113px;font-size:12px;font-weight:700;color:var(--orange-dark);display:flex;align-items:center;gap:7px}
.feature:last-child .read-more{left:15px}
.plus{width:15px;height:15px;background:var(--orange);border-radius:2px;color:var(--white);font-size:14px;line-height:15px;text-align:center}

.card{background:linear-gradient(var(--white),#f0f0f0);border:1px solid #e4e4e4;border-radius:4px;box-shadow:0 1px 2px rgba(0,0,0,.12)}
.testimonial{left:130px;top:636px;width:619px;height:80px}
.avatar{left:130px;top:624px;width:102px;height:102px;border-radius:50%;border:4px solid #8d8d8d;background:radial-gradient(circle,#b89a86,#5b5552);box-shadow:0 2px 4px rgba(0,0,0,.35)}
.quote{left:254px;top:655px;font-size:16px;font-weight:700}
.quote-by{left:313px;top:678px;font-size:14px;color:#888}
.quote-by b{color:#555}
.blog{left:768px;top:636px;width:301px;height:80px;text-align:center}
.blog h3{font-size:16px;margin-top:19px}
.blog p{font-size:14px;color:#888;margin-top:5px}
.blog p b{color:#555}
.blog .arr{color:var(--orange);font-weight:700;position:absolute;top:41px;font-size:14px}

.panel{top:742px;width:301px;height:146px;background:var(--white);border:1px solid #e4e4e4;border-radius:4px;overflow:hidden}
.panel-head{height:36px;background:linear-gradient(var(--panel-head-top),var(--panel-head-bottom));color:var(--white);font-weight:700;font-size:14px;line-height:37px;padding-left:19px}
.panel ul{list-style:none;padding:11px 0 0 19px}
.panel li{font-size:14px;line-height:20px;color:#8a8a8a;white-space:nowrap}
.alerts li{font-weight:700}
.mark{color:var(--orange);margin-right:7px;font-weight:700}
.news li b{color:#555}

.footer-rule{left:130px;top:909px;width:940px;height:1px;background:var(--line)}
.copyright{left:130px;top:924px;width:299px;height:33px;background:var(--footer-dark);border-radius:4px 4px 0 0;color:#ccc;font-size:13px;line-height:35px;padding-left:15px}
.copyright b{color:var(--brand-blue)}
.footer-links{left:449px;top:933px;font-size:13px;color:#888}
.social{right:130px;top:924px;display:flex;gap:4px}
.social span{height:24px;padding:0 3px;border-radius:3px;background:var(--social-blue);color:var(--white);font-size:7px;line-height:24px}
.social span.orb{background:var(--social-red)}
.bottom-strip{left:0;top:957px;width:1200px;height:6px;background:#3a3a3a}
</style>
</head>
<body>
<header class="abs site-header"></header>
<div class="abs brand"><span class="brand-dot"></span><span class="brand-name">Prospix</span></div>

<nav class="abs main-nav">
  <span class="nav-item active" style="left:255px;width:68px">New</span>
  <span class="nav-item" style="left:323px;width:76px">People</span>
  <span class="nav-item" style="left:399px;width:100px">Companies</span>
  <span class="nav-item" style="left:499px;width:99px">Downloads</span>
</nav>
<div class="abs search">search</div>

<div class="abs login-box">
  <div class="login-tabs"><span class="tab-login">Account Login</span><span class="tab-signup">Free Sign Up</span></div>
  <div class="login-field" style="top:35px">username</div>
  <div class="login-field" style="top:73px">password</div>
</div>

<section class="abs hero" role="img" aria-label="Photo of business colleagues reviewing sales data together">
  <div class="abs hero-title">New Opportunities.</div>
  <div class="abs hero-sub">Market Knowledge.</div>
  <div class="abs cta">Try it free</div>
  <div class="abs slide-arrow prev">❮</div>
  <div class="abs slide-arrow next">❯</div>
</section>

<section class="abs features">
  <article class="feature" style="width:310px">
    <h2>Fresh Data</h2>
    <p>Lorem ipsum dolor sit amet, sectetur <b>adipiscing elit</b>. Nullam et tellus quam, vel malesuada metus.</p>
    <span class="read-more"><span class="plus">+</span>Read more</span>
  </article>
  <article class="feature" style="width:319px;padding-left:13px">
    <h2>Sales Intelligence</h2>
    <p>Nullam malesuada est odio, ut convallis quam. Vivamus viverra elit eu nisl <b>ullamcorper</b> et tristique ante vehicula.</p>
    <span class="read-more" style="left:13px"><span class="plus">+</span>Read more</span>
  </article>
  <article class="feature" style="width:311px">
    <h2>Increased Bottomline</h2>
    <p>Nulla sodales, nisi et placerat imperdiet, tellus elit <b>mattis</b> sem, nec <b>ultricies</b> est tortor nec diam.</p>
    <span class="read-more"><span class="plus">+</span>Read more</span>
  </article>
</section>

<div class="abs card testimonial"></div>
<div class="abs avatar" role="img" aria-label="Portrait of the quoted customer"></div>
<p class="abs quote">"My sales have increased 25% due to your website."</p>
<p class="abs quote-by"><b>Marcus Delane</b> Sales Executive Prospix</p>

<div class="abs card blog">
  <h3>Blog:</h3>
  <p><b>12/11:</b> CopyHarbor scores $2.5M</p>
  <span class="arr" style="left:10px">❮</span><span class="arr" style="right:11px">❯</span>
</div>

<section class="abs panel alerts" style="left:130px">
  <div class="panel-head">» TODAY'S ALERTS</div>
  <ul>
    <li><span class="mark">+</span>Brightreel Gets $5M Funding</li>
    <li><span class="mark">+</span>Lumacore Optics Hires VP NA Sales</li>
    <li><span class="mark">+</span>Orbinet Gets $20M Contract</li>
    <li><span class="mark">+</span>Announces Hiring Plan</li>
  </ul>
</section>
<section class="abs panel lists" style="left:449px">
  <div class="panel-head">» EXECUTIVE LISTS</div>
  <ul>
    <li><span class="mark">✔</span>Emails included</li>
    <li><span class="mark">✔</span>Top US Company Executives</li>
    <li><span class="mark">✔</span>See our Delivery Guarantee</li>
    <li><span class="mark">✔</span>CEO, CFO, COO, VP, etc</li>
  </ul>
</section>
<section class="abs panel news" style="left:768px">
  <div class="panel-head">» NEWS/AWARDS</div>
  <ul>
    <li><span class="mark" style="margin-right:2px">&gt;</span><b>11/27: 2012</b> Technology 200!</li>
    <li><span class="mark" style="margin-right:2px">&gt;</span><b>07/17: 2012</b> Colorado Awardees</li>
    <li><span class="mark" style="margin-right:2px">&gt;</span><b>07/03: 2012</b> Pennsylvania Awardees</li>
    <li><span class="mark" style="margin-right:2px">&gt;</span><b>06/19: 2012</b> Midwest Awardees</li>
  </ul>
</section>

<div class="abs footer-rule"></div>
<footer class="abs copyright">© Copyright 2013 <b>Prospix</b>. Rights Reserved.</footer>
<p class="abs footer-links">People | Companies | SiteMap</p>
<div class="abs social">
  <span>chatterlane</span><span>quipstream</span><span class="orb">orbitly+</span><span>workNest</span>
</div>
<div class="abs bottom-strip"></div>
</body>
</html>
```